Crestmoor Valor Cleaning Solutions

Need a logo and business card design. I want to use a translucent business card. I want to abbreviate the name C.V.C.S. Commercial Cleaning, because my is Tam. I’d also like to incorporate a knight or something like that. I want the idea to tie in with the word Crestmoor. New ideas are welcome, i don’t want to limit anyone’s creativity.

Target Market(s)

Commercial Cleaning for businesses.

Contact Information for Business Card

Crestmoor
Valor
Cleaning
Solutions

```html
<!DOCTYPE html>
<html lang="en">
<head>
<meta charset="utf-8">
<title>Crestmoor Valor Cleaning Solutions – Business Card</title>
<link href="https://fonts.googleapis.com/css2?family=Roboto:wght@300;400;700&display=swap" rel="stylesheet">
<style>
  :root {
    --page-bg: #eceff2;
    --card-frost: #e4e8ec;
    --card-frost-edge: #d3d9df;
    --accent-blue: #2ea3e0;
    --name-blue: #45a9e6;
    --text-light: #e8eef6;
    --divider: rgba(255, 255, 255, 0.22);
    --brand-navy: #0f2a5a;
  }
  html, body {
    margin: 0;
    padding: 0;
    width: 1200px;
    height: 970px;
    overflow: hidden;
    background: var(--page-bg);
    font-family: "Roboto", Arial, sans-serif;
  }
  .card {
    position: absolute;
    left: 100px;
    top: 207px;
    width: 1000px;
    height: 556px;
    border-radius: 24px;
    overflow: hidden;
    background: linear-gradient(135deg, var(--card-frost) 0%, #eef1f4 55%, var(--card-frost-edge) 100%);
    box-shadow: 0 10px 30px rgba(20, 40, 70, 0.12);
  }
  .card-shapes {
    position: absolute;
    inset: 0;
  }
  .contact-panel {
    position: absolute;
    left: 71px;
    top: 0;
    width: 340px;
    color: var(--text-light);
  }
  .person-name {
    position: absolute;
    top: 96px;
    margin: 0;
    font-size: 34px;
    font-weight: 700;
    color: var(--name-blue);
    letter-spacing: 0.3px;
    white-space: nowrap;
  }
  .person-title {
    position: absolute;
    top: 140px;
    margin: 0;
    font-size: 22px;
    font-weight: 300;
    white-space: nowrap;
  }
  .divider {
    position: absolute;
    left: 0;
    width: 322px;
    height: 1px;
    background: var(--divider);
  }
  .divider.top { top: 200px; }
  .divider.bottom { top: 358px; }
  .contact-list {
    position: absolute;
    top: 232px;
    margin: 0;
    padding: 0;
    list-style: none;
    font-size: 22px;
    font-weight: 300;
    line-height: 32px;
    white-space: nowrap;
  }
  .contact-list .label {
    color: var(--name-blue);
    font-weight: 700;
  }
  .address {
    position: absolute;
    top: 389px;
    margin: 0;
    font-style: normal;
    font-size: 22px;
    font-weight: 300;
    line-height: 32px;
    white-space: nowrap;
  }
  .brand-name {
    position: absolute;
    left: 560px;
    top: 238px;
    width: 380px;
    margin: 0;
    text-align: center;
    color: var(--brand-navy);
    font-size: 32px;
    font-weight: 700;
    line-height: 40px;
  }
</style>
</head>
<body>
  <div class="card">
    <svg class="card-shapes" width="1000" height="556" viewBox="0 0 1000 556" aria-hidden="true">
      <defs>
        <linearGradient id="panelGradient" x1="0" y1="0" x2="1" y2="0.3">
          <stop offset="0" stop-color="#3a5f8f"/>
          <stop offset="0.55" stop-color="#123672"/>
          <stop offset="1" stop-color="#0a2a63"/>
        </linearGradient>
      </defs>
      <path d="M0 0 H650 Q315 278 600 556 H0 Z" fill="var(--accent-blue)"/>
      <path d="M0 0 H600 Q320 278 600 556 H0 Z" fill="url(#panelGradient)"/>
    </svg>

    <div class="contact-panel">
      <h1 class="person-name">JORDAN WELBECK</h1>
      <p class="person-title">General Manager</p>
      <div class="divider top"></div>
      <ul class="contact-list">
        <li><span class="label">T:</span> +1-555-214-7730</li>
        <li><span class="label">E:</span> info@cvcscleaning.com</li>
        <li><span class="label">W:</span> www.cvcscleaning.com</li>
      </ul>
      <div class="divider bottom"></div>
      <address class="address">41 Harrow Ridge Road<br>Fenwick, CT 06099</address>
    </div>

    <p class="brand-name">Crestmoor Valor<br>Cleaning Solutions</p>
  </div>
</body>
</html>
```